Cousin Fenwick's Filmaro Project

Create a design with the words, "Cousin Fenwick's Fil-maro Kit". This design will be featured on the product itself. The product will entail a kit of items to help auto body and painters make repairs. The kit itself will be at least one foot long/wide when packaged.

The design should be more than just the logo....it will need to be on the cover of the product which is approx 8" by 8".

Target Market(s)

Anyone who repairs fiberglass, hard surface products for a living...auto, boats, decks, drywall, etc. Largely blue collar DIY men.

Requirements
Must have
• Some of the design must have a see-through/clear section so that customers can see what is in the package.
Nice to have
• In an ideal world, the design could be expanded or shrunk but should be about 1" high.
Should not have
• No cartoon characters.

```html
<!DOCTYPE html>
<html lang="en">
<head>
<meta charset="utf-8">
<title>Cousin Fenwick's Fil-maro Kit</title>
<link rel="stylesheet" href="https://fonts.googleapis.com/css2?family=Montserrat:wght@300;500;600&display=swap">
<style>
  :root {
    --backdrop: #e9e9e9;
    --bag-navy: #141c3e;
    --bag-navy-deep: #0a0f26;
    --bag-sheen: #2a3766;
    --window-tint: rgba(190, 200, 230, 0.28);
    --window-edge: rgba(220, 228, 250, 0.55);
    --seam: #1c2a5c;
    --ink-white: #f2f2f2;
    --ink-soft: #c9ccd8;
  }
  * { margin: 0; padding: 0; box-sizing: border-box; }
  html, body {
    width: 1200px;
    height: 789px;
    overflow: hidden;
    background: var(--backdrop);
  }
  .canvas {
    position: relative;
    width: 1200px;
    height: 789px;
    display: flex;
    align-items: center;
    justify-content: center;
  }
  .bag-face {
    position: relative;
    width: 600px;
    height: 720px;
    background: radial-gradient(ellipse at 50% 60%, var(--bag-sheen) 0%, var(--bag-navy) 50%, var(--bag-navy-deep) 100%);
    font-family: "Montserrat", sans-serif;
    color: var(--ink-white);
    text-align: center;
  }
  .handle-slot {
    position: absolute;
    top: 120px;
    left: 50%;
    transform: translateX(-50%);
    width: 96px;
    height: 50px;
    border-radius: 25px;
    background: var(--backdrop);
  }
  .brand-name {
    position: absolute;
    top: 225px;
    left: 0;
    right: 0;
    font-weight: 500;
    font-size: 36px;
    line-height: 1.3;
    letter-spacing: 0.05em;
    text-transform: uppercase;
    color: var(--ink-white);
  }
  .clear-window {
    position: absolute;
    top: 348px;
    left: 95px;
    width: 410px;
    height: 150px;
    border-radius: 75px;
    background: radial-gradient(ellipse at 50% 45%, rgba(230, 236, 255, 0.38) 0%, var(--window-tint) 55%, rgba(190, 200, 230, 0.12) 100%);
    border: 1.5px solid var(--window-edge);
  }
  .tagline {
    position: absolute;
    top: 525px;
    left: 0;
    right: 0;
  }
  .tagline-lead {
    font-weight: 300;
    font-size: 19px;
    letter-spacing: 0.1em;
    text-transform: uppercase;
    color: var(--ink-soft);
  }
  .tagline-uses {
    margin-top: 10px;
    font-weight: 600;
    font-size: 15px;
    letter-spacing: 0.07em;
    text-transform: uppercase;
  }
  .use-icons {
    position: absolute;
    top: 610px;
    left: 0;
    right: 0;
    display: flex;
    justify-content: center;
    gap: 36px;
  }
  .use-icons svg { width: 34px; height: 34px; fill: var(--ink-white); stroke: var(--ink-white); }
  .bottom-seam {
    position: absolute;
    left: 0;
    right: 0;
    bottom: 0;
    height: 34px;
    background: var(--seam);
  }
</style>
</head>
<body>
<main class="canvas">
  <section class="bag-face">
    <div class="handle-slot"></div>

    <h1 class="brand-name">Cousin Fenwick's<br>Fil-maro Kit</h1>

    <div class="clear-window" role="img" aria-label="Clear see-through window showing the repair kit contents"></div>

    <div class="tagline">
      <p class="tagline-lead">Repair fiberglass to:</p>
      <p class="tagline-uses">Auto, boats, decks, drywall and more!</p>
    </div>

    <div class="use-icons">
      <svg class="icon-auto" viewBox="0 0 30 30" aria-label="Auto">
        <path stroke="none" d="M6 12 L9 5 H21 L24 12 H26 V23 H22 V20 H8 V23 H4 V12 Z M10 7 L8 12 H22 L20 7 Z"/>
        <circle cx="9" cy="16" r="1.6" fill="var(--bag-navy)" stroke="none"/>
        <circle cx="21" cy="16" r="1.6" fill="var(--bag-navy)" stroke="none"/>
      </svg>
      <svg class="icon-boat" viewBox="0 0 30 30" aria-label="Boats">
        <path stroke="none" d="M12 3 H18 V7 H21 V12 L25 14 L22 21 H8 L5 14 L9 12 V7 H12 Z"/>
        <path fill="none" stroke-width="1.5" d="M3 24 q3 -2 6 0 t6 0 t6 0 t6 0 M3 28 q3 -2 6 0 t6 0 t6 0 t6 0"/>
      </svg>
      <svg class="icon-deck" viewBox="0 0 30 30" aria-label="Decks">
        <path stroke="none" d="M3 10 H27 L25 20 H5 Z"/>
        <path fill="none" stroke="var(--bag-navy)" stroke-width="1.4" d="M9 10 V20 M13.5 10 V20 M18 10 V20 M22 10 V20"/>
      </svg>
      <svg class="icon-drywall" viewBox="0 0 30 30" aria-label="Drywall">
        <path fill="none" stroke-width="2" d="M10 3 V27 M19 3 V27 M3 11 H27 M3 19 H27"/>
      </svg>
    </div>

    <div class="bottom-seam"></div>
  </section>
</main>
</body>
</html>
```